TR Stationery - Modern Contemporary

Develop modern template for Letterhead and Stationery (business card, letterhead, envelopes) using the TR Logo and Icon

Colors
0054AA
0677BA
7BADD7
CADEEF
E8F1F8
00AB8E
00BBA5
67D7C9
C6EFE9
E9F9F6
EE7325
F08F49
F5BC92
FAE3D3
FDF4ED
6B429C
8869AF
B7A5CE
E3DAEB
F3F0F8

```html
<!DOCTYPE html>
<html lang="en">
<head>
<meta charset="utf-8">
<title>Tessa Rovi – Business Card</title>
<link rel="stylesheet" href="https://fonts.googleapis.com/css2?family=Open+Sans:wght@400;600;700&display=swap">
<style>
  :root {
    --backdrop: #e6e6e6;
    --card: #ffffff;
    --navy: #262a44;
    --navy-card: #2c3049;
    --green: #2bbf7f;
    --orange: #f5822a;
    --black: #0a0a0a;
    --body-text: #555555;
    --mark-light: #9aa0d6;
  }
  * { margin: 0; padding: 0; box-sizing: border-box; }
  html, body { width: 1133px; height: 1200px; overflow: hidden; }
  body {
    background: var(--backdrop);
    font-family: "Open Sans", Arial, sans-serif;
    position: relative;
  }
  .card {
    position: absolute;
    left: 186px;
    width: 760px;
    height: 433px;
  }
  .card-front { top: 110px; background: var(--card); }
  .card-back { top: 620px; background: var(--navy-card); }

  .wordmark {
    position: absolute;
    font-family: "Open Sans", Arial, sans-serif;
    font-weight: 600;
    color: var(--navy);
    white-space: nowrap;
    letter-spacing: 0.5px;
  }
  .card-front .wordmark { left: 64px; top: 178px; font-size: 44px; line-height: 60px; }
  .card-back .wordmark {
    left: 0; right: 0; top: 170px; text-align: center;
    font-size: 76px; line-height: 90px; color: var(--mark-light);
  }

  .holder { position: absolute; left: 429px; top: 78px; }
  .holder-name { font-size: 25px; font-weight: 700; color: var(--navy); line-height: 30px; letter-spacing: 0.3px; }
  .holder-name .surname { color: var(--green); }
  .holder-role { font-size: 17px; color: var(--orange); line-height: 22px; }

  .divider { position: absolute; top: 153px; height: 3px; }
  .divider-black { left: 434px; width: 84px; background: var(--black); }
  .divider-green { left: 522px; width: 85px; background: var(--green); }
  .divider-orange { left: 611px; width: 85px; background: var(--orange); }

  .contact-row { position: absolute; left: 430px; display: flex; align-items: center; }
  .contact-row svg { width: 30px; height: 30px; flex: none; }
  .contact-text { margin-left: 10px; font-size: 17px; line-height: 21px; color: var(--body-text); }
  .row-address { top: 182px; }
  .row-phone { top: 240px; }
  .row-web { top: 305px; }

  .band { position: absolute; bottom: 0; height: 11px; }
  .band-black { left: 0; width: 250px; background: var(--black); }
  .band-green { left: 255px; width: 250px; background: var(--green); }
  .band-orange { left: 510px; width: 250px; background: var(--orange); }
</style>
</head>
<body>

<section class="card card-front">
  <div class="wordmark">tessa rovi</div>

  <div class="holder">
    <div class="holder-name">DANIEL <span class="surname">REYES</span></div>
    <div class="holder-role">President</div>
  </div>

  <div class="divider divider-black"></div>
  <div class="divider divider-green"></div>
  <div class="divider divider-orange"></div>

  <div class="contact-row row-address">
    <svg viewBox="0 0 30 30" aria-hidden="true">
      <circle cx="15" cy="15" r="15" fill="var(--orange)"/>
      <path d="M15 7.5a5 5 0 0 0-5 5c0 3.8 5 9.5 5 9.5s5-5.7 5-9.5a5 5 0 0 0-5-5z" fill="none" stroke="#fff" stroke-width="1.6"/>
      <circle cx="15" cy="12.5" r="1.8" fill="#fff"/>
    </svg>
    <div class="contact-text">1240 Cedar Hollow Road<br>Juneau, Alaska 34810</div>
  </div>

  <div class="contact-row row-phone">
    <svg viewBox="0 0 30 30" aria-hidden="true">
      <circle cx="15" cy="15" r="15" fill="var(--orange)"/>
      <path d="M10.5 8.5l2.4-.4 1.4 3.3-1.6 1.2c.8 1.8 2.1 3.1 3.9 3.9l1.2-1.6 3.3 1.4-.4 2.4c-.2.8-.9 1.3-1.7 1.2-5.1-.5-9.1-4.5-9.6-9.6-.1-.8.4-1.5 1.1-1.8z" fill="#fff"/>
    </svg>
    <div class="contact-text">555-204-1187<br>555-318-6642</div>
  </div>

  <div class="contact-row row-web">
    <svg viewBox="0 0 30 30" aria-hidden="true">
      <circle cx="15" cy="15" r="15" fill="var(--orange)"/>
      <circle cx="15" cy="15" r="6.5" fill="none" stroke="#fff" stroke-width="1.6"/>
      <path d="M11 11.5c1.5.3 2.3 1.3 2 2.6-.2 1 1 1.5 1.4 2.6.3.9-.2 2-.9 2.6M17.5 9.3c-.5 1.2.2 2.2 1.4 2.3 1 .1 1.6.8 1.8 1.7" fill="none" stroke="#fff" stroke-width="1.4"/>
    </svg>
    <div class="contact-text">name@tessarovi.com<br>www.tessarovi.com</div>
  </div>

  <div class="band band-black"></div>
  <div class="band band-green"></div>
  <div class="band band-orange"></div>
</section>

<section class="card card-back">
  <div class="wordmark">tessa rovi</div>
</section>

</body>
</html>
```